Business Card Design Brookvale Flooring

We are a Mobile Flooring Company servicing the Central Coast NSW and Newcastle.We sell and Install Bamboo flooring, laminate flooring and engineered flooring to do it yourself renovators, builders and home improvement clientsOur prices are very competitive and we have a great colour range and selection.We would like the front of the card to have the wood floorboard image (perhaps as the background) and then have our logo over the top (large) with the logo in spot gloss and all the writing in spot gloss. Details of what we do can be included on the back with the deer image (perhaps in silhouette) in the background. Any other ideas using these images will be appreciated.

Target Market(s)

DIY renovators, builders, home improvement clients

Industry/Entity Type

Flooring

Contact Information for Business Card

Servicing Central Coast to Newcastle
sales@brookvaleflooring.com.au
0438 216 504
www.brookvaleflooring.com.au

Font styles to use
Other font styles liked:
• You decide

Requirements
Must have
• The project must have both files uploaded on the business card the image of the woodland forest/ floorboards in the background - filling the whole business card or half business card with the logo over the top
• The logo and all the writing needs to be spot gloss
Nice to have
• A clear easy to read attractive business card
Should not have
• Too dark

```html
<!DOCTYPE html>
<html lang="en">
<head>
<meta charset="utf-8">
<title>Brookvale Flooring – Business Card</title>
<link rel="stylesheet" href="https://fonts.googleapis.com/css2?family=Arimo:wght@400;700&display=swap">
<style>
  :root {
    --page-bg: #ecebe8;
    --amber: #c98a4e;
    --amber-light: #dba36a;
    --amber-dark: #9a6231;
    --rim: #6b4a2e;
    --wood-light: #ece7df;
    --wood-mid: #d9c8ae;
    --wood-warm: #c99a63;
    --ink-dark: #3a2a1e;
    --ink-light: #ffffff;
    --icon-bg: #2d241d;
  }
  * { margin: 0; padding: 0; box-sizing: border-box; }
  html, body { width: 1200px; height: 885px; overflow: hidden; }
  body {
    background: var(--page-bg);
    font-family: "Arimo", Arial, sans-serif;
    position: relative;
  }
  .card {
    position: absolute;
    left: 250px;
    width: 700px;
    height: 400px;
    border-radius: 6px;
    overflow: hidden;
    box-shadow: 0 6px 18px rgba(0,0,0,.18);
  }
  .card--front { top: 30px; }
  .card--back { top: 455px; }
  .card__art { position: absolute; inset: 0; width: 100%; height: 100%; }

  .brand {
    position: absolute;
    font-weight: 700;
    letter-spacing: -0.5px;
    display: flex;
    align-items: center;
    gap: 12px;
  }
  .brand__dot {
    width: 14px; height: 14px; border-radius: 50%;
    background: currentColor;
  }
  .card--front .brand {
    right: 48px; top: 96px;
    font-size: 38px;
    color: var(--ink-light);
  }
  .card--back .brand {
    left: 300px; top: 170px;
    font-size: 44px;
    color: var(--ink-dark);
  }

  .contact {
    position: absolute;
    left: 290px; bottom: 56px;
    list-style: none;
    color: var(--ink-light);
    font-size: 19px;
    line-height: 1;
  }
  .contact__item {
    display: flex; align-items: center; gap: 14px;
    margin-top: 12px;
  }
  .contact__icon {
    width: 20px; height: 20px;
    background: var(--icon-bg);
    border-radius: 3px;
    flex: none;
  }
</style>
</head>
<body>

<section class="card card--front" aria-label="Business card, contact side">
  <svg class="card__art" viewBox="0 0 700 400" preserveAspectRatio="none">
    <defs>
      <linearGradient id="woodFront" x1="0" y1="0" x2="1" y2="1">
        <stop offset="0" stop-color="var(--wood-warm)"/>
        <stop offset=".45" stop-color="var(--wood-mid)"/>
        <stop offset="1" stop-color="var(--wood-light)"/>
      </linearGradient>
      <linearGradient id="amberFront" x1="0" y1="0" x2="1" y2="0">
        <stop offset="0" stop-color="var(--amber-dark)"/>
        <stop offset=".4" stop-color="var(--amber-light)"/>
        <stop offset="1" stop-color="var(--amber)"/>
      </linearGradient>
    </defs>
    <rect class="wood-panel" width="700" height="400" fill="url(#woodFront)" role="img" aria-label="Light end-grain timber texture"/>
    <path class="wave-rim" d="M190 0 C 300 90, 130 230, 240 400 L700 400 L700 0 Z" fill="var(--rim)"/>
    <path class="wave-panel" d="M202 0 C 312 90, 142 230, 252 400 L700 400 L700 0 Z" fill="url(#amberFront)"/>
  </svg>

  <div class="brand"><span class="brand__dot"></span>Brookvale Flooring</div>

  <ul class="contact">
    <li class="contact__item">
      <svg class="contact__icon" viewBox="0 0 20 20" aria-hidden="true"><rect width="20" height="20" rx="3" fill="var(--icon-bg)"/><path d="M6 4h3l1 3-2 1a8 8 0 0 0 4 4l1-2 3 1v3a2 2 0 0 1-2 2A11 11 0 0 1 4 6a2 2 0 0 1 2-2z" fill="#fff"/></svg>
      0438 216 504
    </li>
    <li class="contact__item">
      <svg class="contact__icon" viewBox="0 0 20 20" aria-hidden="true"><rect width="20" height="20" rx="3" fill="var(--icon-bg)"/><circle cx="10" cy="10" r="6" fill="none" stroke="#fff" stroke-width="1.4"/><path d="M4 10h12M10 4c-3 3-3 9 0 12M10 4c3 3 3 9 0 12" fill="none" stroke="#fff" stroke-width="1.2"/></svg>
      www.brookvaleflooring.com.au
    </li>
    <li class="contact__item">
      <svg class="contact__icon" viewBox="0 0 20 20" aria-hidden="true"><rect width="20" height="20" rx="3" fill="var(--icon-bg)"/><rect x="4" y="6" width="12" height="8" fill="none" stroke="#fff" stroke-width="1.4"/><path d="M4 6l6 5 6-5" fill="none" stroke="#fff" stroke-width="1.4"/></svg>
      sales@brookvaleflooring.com.au
    </li>
  </ul>
</section>

<section class="card card--back" aria-label="Business card, logo side">
  <svg class="card__art" viewBox="0 0 700 400" preserveAspectRatio="none">
    <defs>
      <radialGradient id="woodBack" cx=".55" cy=".35" r=".8">
        <stop offset="0" stop-color="#f6f3ee"/>
        <stop offset=".7" stop-color="var(--wood-light)"/>
        <stop offset="1" stop-color="var(--wood-mid)"/>
      </radialGradient>
      <linearGradient id="amberBack" x1="0" y1="0" x2="1" y2="1">
        <stop offset="0" stop-color="var(--amber-dark)"/>
        <stop offset=".5" stop-color="var(--amber-light)"/>
        <stop offset="1" stop-color="var(--amber)"/>
      </linearGradient>
    </defs>
    <rect class="amber-panel" width="700" height="400" fill="url(#amberBack)"/>
    <path class="wave-rim" d="M0 0 L700 0 L700 400 L560 400 C 420 300, 260 360, 170 200 C 110 100, 40 80, 0 70 Z" fill="var(--rim)"/>
    <path class="wood-panel" d="M0 0 L700 0 L700 400 L580 400 C 430 290, 280 345, 185 190 C 125 95, 50 68, 0 58 Z" fill="url(#woodBack)" role="img" aria-label="Pale end-grain timber texture"/>
  </svg>

  <div class="brand"><span class="brand__dot"></span>Brookvale Flooring</div>
</section>

</body>
</html>
```